Multi Disciplinary Health Clinic Needs a Pop Up Banner

Brightway Health needs a pop up banner ( approx. 33" x 80") to use at marketing events. We offer Chiropractic, Massage Therapy, Acupuncture, Laser Therapy, Shockwave Therapy and a lot of other modalities. We have a diverse client base ranging from children to professional athletes. More info about our clinic can be found at www.brightwayhealth.ca

Target Market(s)

potential patients, all age ranges, people who are in pain or are wanting to improve their health

Industry/Entity Type

Health And Wellness

Font styles to use
Sans Serif

Requirements
Must have
• our logo
• serives: chiropractic, massage therapy, shockwave, laser
• our logo colours as the basis for the colour theme
• our website address
Nice to have
• our phone number
• images from our website ( i have high resolution files of all images)
• word font that fits with our logo font
Should not have
• an abundance of spa massage pictures. we focus more on the rehabilitation of pain and injury.

```html
<!DOCTYPE html>
<html lang="en">
<head>
<meta charset="utf-8">
<title>Brightway Health – Pop Up Banner</title>
<link rel="stylesheet" href="https://fonts.googleapis.com/css2?family=Didact+Gothic&family=Ubuntu:wght@400&family=Open+Sans:wght@300;400&display=swap">
<style>
  :root {
    --brand-blue: #0b63a6;
    --ink-blue: #1366a9;
    --ring-grey: #6c7176;
    --stripe-grey: #c9cbcc;
    --text-grey: #5f6468;
    --gap-grey: #d4d4d4;
    --white: #ffffff;
  }
  * { margin: 0; padding: 0; box-sizing: border-box; }
  html, body { width: 1040px; height: 1200px; overflow: hidden; }
  body { background: var(--gap-grey); position: relative; font-family: "Didact Gothic", sans-serif; }

  .banner { position: absolute; top: 0; width: 495px; height: 1200px; background: var(--white); overflow: hidden; }
  .banner--a { left: 0; }
  .banner--b { left: 545px; }
  .banner__art { position: absolute; inset: 0; }

  .brand { position: absolute; top: 56px; left: 0; width: 495px; display: flex; justify-content: center; align-items: center; gap: 12px; color: var(--brand-blue); font-family: "Didact Gothic", sans-serif; font-size: 42px; line-height: 1; }
  .brand__dot { width: 30px; height: 30px; border-radius: 50%; background: var(--brand-blue); }

  .tagline { position: absolute; left: 0; width: 495px; text-align: center; color: var(--white); font-family: "Ubuntu", sans-serif; line-height: 1; }
  .tagline--lead { top: 170px; font-size: 37px; letter-spacing: 0.5px; }
  .tagline--main { top: 217px; font-size: 56px; letter-spacing: 1px; }

  .service { position: absolute; color: var(--ink-blue); font-size: 33px; line-height: 1; white-space: nowrap; letter-spacing: 0.3px; }
  .service--left { left: 204px; }
  .service--right { right: 207px; text-align: right; }
  .service--chiro { top: 379px; }
  .service--acu { top: 497px; }
  .service--massage { top: 616px; }
  .service--laser { top: 742px; }
  .service--shock { top: 864px; }

  .extras__title { position: absolute; top: 950px; left: 0; width: 500px; text-align: center; color: var(--text-grey); font-size: 21px; line-height: 1; }
  .extras__item { position: absolute; color: var(--text-grey); font-size: 20.5px; line-height: 1; white-space: nowrap; letter-spacing: 0.3px; }
  .row-1 { top: 984px; }
  .row-2 { top: 1017px; }
  .col-a { left: 22px; }
  .col-sep { left: 276px; }
  .col-b { left: 297px; }

  .billing { position: absolute; top: 1062px; left: 0; width: 495px; text-align: center; color: var(--ink-blue); font-size: 22.5px; line-height: 1; letter-spacing: 0.3px; }

  .contact { position: absolute; top: 1106px; left: 0; width: 495px; display: flex; justify-content: center; align-items: baseline; gap: 4px; color: var(--white); font-family: "Open Sans", sans-serif; font-weight: 300; line-height: 1; }
  .contact__label { font-size: 17px; font-weight: 400; }
  .contact__phone { font-size: 43px; }
  .website { position: absolute; top: 1164px; left: 0; width: 495px; text-align: center; color: var(--ink-blue); font-size: 23.5px; line-height: 1; letter-spacing: 0.5px; }
</style>
</head>
<body>

<section class="banner banner--a">
  <svg class="banner__art" width="495" height="1200" viewBox="0 0 495 1200">
    <defs>
      <linearGradient id="a-chiro" x1="0" y1="0" x2="1" y2="1"><stop offset="0" stop-color="#e9e3df"/><stop offset="1" stop-color="#e58a9e"/></linearGradient>
      <linearGradient id="a-acu" x1="0" y1="0" x2="1" y2="1"><stop offset="0" stop-color="#f2f2f2"/><stop offset="1" stop-color="#e7c4ae"/></linearGradient>
      <linearGradient id="a-mass" x1="0" y1="0" x2="1" y2="1"><stop offset="0" stop-color="#e7d9c6"/><stop offset="1" stop-color="#2a2d3a"/></linearGradient>
      <linearGradient id="a-laser" x1="0" y1="0" x2="1" y2="1"><stop offset="0" stop-color="#c9ccd0"/><stop offset="1" stop-color="#d9a78c"/></linearGradient>
      <linearGradient id="a-shock" x1="0" y1="0" x2="1" y2="1"><stop offset="0" stop-color="#bcd3e6"/><stop offset="1" stop-color="#e0a07c"/></linearGradient>
    </defs>
    <path d="M0,104 Q247,216 495,104 L495,284 L0,284 Z" fill="var(--brand-blue)"/>
    <rect x="0" y="284" width="495" height="10" fill="var(--stripe-grey)"/>

    <g stroke="var(--ink-blue)" stroke-width="1.6" stroke-dasharray="1.6 2.4">
      <line x1="204" y1="416" x2="493" y2="416"/>
      <line x1="0" y1="538" x2="288" y2="538"/>
      <line x1="204" y1="657" x2="493" y2="657"/>
      <line x1="0" y1="782" x2="288" y2="782"/>
      <line x1="204" y1="904" x2="493" y2="904"/>
      <line x1="22" y1="976" x2="474" y2="976"/>
      <line x1="22" y1="1052" x2="474" y2="1052"/>
    </g>

    <circle cx="100" cy="394" r="86" fill="var(--ring-grey)"/>
    <circle cx="104" cy="398" r="82" fill="var(--white)"/>
    <circle cx="104" cy="398" r="79" fill="url(#a-chiro)" role="img" aria-label="Chiropractor adjusting a patient's shoulder"/>

    <circle cx="394" cy="514" r="86" fill="var(--ring-grey)"/>
    <circle cx="390" cy="518" r="82" fill="var(--white)"/>
    <circle cx="390" cy="518" r="79" fill="url(#a-acu)" role="img" aria-label="Acupuncture treatment"/>

    <circle cx="100" cy="634" r="86" fill="var(--ring-grey)"/>
    <circle cx="104" cy="638" r="82" fill="var(--white)"/>
    <circle cx="104" cy="638" r="79" fill="url(#a-mass)" role="img" aria-label="Therapeutic shoulder massage"/>

    <circle cx="394" cy="760" r="86" fill="var(--ring-grey)"/>
    <circle cx="390" cy="764" r="82" fill="var(--white)"/>
    <circle cx="390" cy="764" r="79" fill="url(#a-laser)" role="img" aria-label="Laser therapy device on a knee"/>

    <circle cx="100" cy="882" r="86" fill="var(--ring-grey)"/>
    <circle cx="104" cy="886" r="82" fill="var(--white)"/>
    <circle cx="104" cy="886" r="79" fill="url(#a-shock)" role="img" aria-label="Shockwave therapy on a patient's shoulder"/>

    <rect x="0" y="1092" width="495" height="6" fill="var(--stripe-grey)"/>
    <rect x="0" y="1098" width="495" height="102" fill="var(--brand-blue)"/>
    <path d="M70,1200 C100,1200 104,1158 138,1158 L392,1158 C430,1158 436,1200 470,1200 Z" fill="var(--white)"/>
  </svg>

  <div class="brand"><span class="brand__dot"></span>Brightway Health</div>
  <p class="tagline tagline--lead">helping you live life</p>
  <p class="tagline tagline--main">pain free</p>

  <p class="service service--left service--chiro">Chiropractic</p>
  <p class="service service--right service--acu">Acupuncture</p>
  <p class="service service--left service--massage">Massage Therapy</p>
  <p class="service service--right service--laser">Laser Therapy</p>
  <p class="service service--left service--shock">Shockwave Therapy</p>

  <p class="extras__title">Other Services</p>
  <span class="extras__item row-1 col-a">Soft Tissue Mobilization</span>
  <span class="extras__item row-1 col-sep">|</span>
  <span class="extras__item row-1 col-b">Instrument Therapy</span>
  <span class="extras__item row-2 col-a">Cupping Technique</span>
  <span class="extras__item row-2 col-sep">|</span>
  <span class="extras__item row-2 col-b">Kinesiology Taping</span>

  <p class="billing">We offer direct billing and online booking.</p>
  <p class="contact"><span class="contact__label">Call us:</span><span class="contact__phone">(403) 555 0142</span></p>
  <p class="website">www.brightwayhealth.ca</p>
</section>

<section class="banner banner--b">
  <svg class="banner__art" width="495" height="1200" viewBox="0 0 495 1200">
    <defs>
      <linearGradient id="b-chiro" x1="0" y1="0" x2="1" y2="1"><stop offset="0" stop-color="#f1f3f4"/><stop offset="1" stop-color="#e8c0a6"/></linearGradient>
      <linearGradient id="b-acu" x1="0" y1="0" x2="1" y2="1"><stop offset="0" stop-color="#f2f2f2"/><stop offset="1" stop-color="#e7c4ae"/></linearGradient>
      <linearGradient id="b-mass" x1="0" y1="0" x2="1" y2="1"><stop offset="0" stop-color="#e7d9c6"/><stop offset="1" stop-color="#2a2d3a"/></linearGradient>
      <linearGradient id="b-laser" x1="0" y1="0" x2="1" y2="1"><stop offset="0" stop-color="#c9ccd0"/><stop offset="1" stop-color="#d9a78c"/></linearGradient>
      <linearGradient id="b-shock" x1="0" y1="0" x2="1" y2="1"><stop offset="0" stop-color="#bcd3e6"/><stop offset="1" stop-color="#e0a07c"/></linearGradient>
    </defs>
    <path d="M0,104 Q247,216 495,104 L495,284 L0,284 Z" fill="var(--brand-blue)"/>
    <rect x="0" y="284" width="495" height="10" fill="var(--stripe-grey)"/>

    <g stroke="var(--ink-blue)" stroke-width="1.6" stroke-dasharray="1.6 2.4">
      <line x1="204" y1="416" x2="493" y2="416"/>
      <line x1="0" y1="538" x2="288" y2="538"/>
      <line x1="204" y1="657" x2="493" y2="657"/>
      <line x1="0" y1="782" x2="288" y2="782"/>
      <line x1="204" y1="904" x2="493" y2="904"/>
      <line x1="22" y1="976" x2="474" y2="976"/>
      <line x1="22" y1="1052" x2="474" y2="1052"/>
    </g>

    <circle cx="100" cy="394" r="86" fill="var(--ring-grey)"/>
    <circle cx="104" cy="398" r="82" fill="var(--white)"/>
    <circle cx="104" cy="398" r="79" fill="url(#b-chiro)" role="img" aria-label="Practitioner treating a patient's ankle"/>

    <circle cx="394" cy="514" r="86" fill="var(--ring-grey)"/>
    <circle cx="390" cy="518" r="82" fill="var(--white)"/>
    <circle cx="390" cy="518" r="79" fill="url(#b-acu)" role="img" aria-label="Acupuncture treatment"/>

    <circle cx="100" cy="634" r="86" fill="var(--ring-grey)"/>
    <circle cx="104" cy="638" r="82" fill="var(--white)"/>
    <circle cx="104" cy="638" r="79" fill="url(#b-mass)" role="img" aria-label="Therapeutic shoulder massage"/>

    <circle cx="394" cy="760" r="86" fill="var(--ring-grey)"/>
    <circle cx="390" cy="764" r="82" fill="var(--white)"/>
    <circle cx="390" cy="764" r="79" fill="url(#b-laser)" role="img" aria-label="Laser therapy device on a knee"/>

    <circle cx="100" cy="882" r="86" fill="var(--ring-grey)"/>
    <circle cx="104" cy="886" r="82" fill="var(--white)"/>
    <circle cx="104" cy="886" r="79" fill="url(#b-shock)" role="img" aria-label="Shockwave therapy on a patient's shoulder"/>

    <rect x="0" y="1092" width="495" height="6" fill="var(--stripe-grey)"/>
    <rect x="0" y="1098" width="495" height="102" fill="var(--brand-blue)"/>
    <path d="M70,1200 C100,1200 104,1158 138,1158 L392,1158 C430,1158 436,1200 470,1200 Z" fill="var(--white)"/>
  </svg>

  <div class="brand"><span class="brand__dot"></span>Brightway Health</div>
  <p class="tagline tagline--lead">helping you live life</p>
  <p class="tagline tagline--main">pain free</p>

  <p class="service service--left service--chiro">Chiropractic</p>
  <p class="service service--right service--acu">Acupuncture</p>
  <p class="service service--left service--massage">Massage Therapy</p>
  <p class="service service--right service--laser">Laser Therapy</p>
  <p class="service service--left service--shock">Shockwave Therapy</p>

  <p class="extras__title">Other Services</p>
  <span class="extras__item row-1 col-a">Soft Tissue Mobilization</span>
  <span class="extras__item row-1 col-sep">|</span>
  <span class="extras__item row-1 col-b">Instrument Therapy</span>
  <span class="extras__item row-2 col-a">Cupping Technique</span>
  <span class="extras__item row-2 col-sep">|</span>
  <span class="extras__item row-2 col-b">Kinesiology Taping</span>

  <p class="billing">We offer direct billing and online booking.</p>
  <p class="contact"><span class="contact__label">Call us:</span><span class="contact__phone">(403) 555 0142</span></p>
  <p class="website">www.brightwayhealth.ca</p>
</section>

</body>
</html>
```